Dental Business Card

I need Dental oriented business cards.
On the front side -
- on the first line, my name:
Dr Marlo Vintner
- on the second line (just underneath):
Doctor of Dental Medicine
- on the third line, or underneath that or in a corner, I would like the address and phone number:
5182 Ch. Birchfield
Montreal QC H2T 4B9
514-629-5074
- other than that i would maybe like a logo of a tooth, but i want it to be subtle and very basic!
- I would like the card to be preferably black or dark grey-ish with the writing in white
On the other side -
- 2-3 lines with the possibility to write the next appointment the box with the lines should be white, with the rest of the card being black

```html
<!DOCTYPE html>
<html lang="en">
<head>
<meta charset="utf-8">
<title>Dr Marlo Vintner – Business Card</title>
<link rel="stylesheet" href="https://fonts.googleapis.com/css2?family=Noto+Sans:ital,wght@0,400;0,700;1,400&display=swap">
<style>
  :root {
    --backdrop: #e2e2e2;
    --ink: #000000;
    --paper: #ffffff;
    --faint: #ececec;
  }
  * { margin: 0; padding: 0; box-sizing: border-box; }
  html, body {
    width: 1200px; height: 1000px; overflow: hidden;
    background: var(--backdrop);
    font-family: "Noto Sans", "DejaVu Sans", Verdana, sans-serif;
  }
  .canvas { position: relative; width: 1200px; height: 1000px; }

  .card { position: absolute; overflow: hidden; }

  /* Appointment side */
  .card--appointment {
    left: 297px; top: 112px; width: 605px; height: 345px;
    background: var(--ink);
  }
  .appointment-heading {
    position: absolute; left: 63px; top: 54px; width: 479px;
    display: flex; align-items: center; gap: 12px;
    color: var(--paper); font-weight: 700; font-size: 23px; letter-spacing: 0.3px;
    white-space: nowrap;
  }
  .appointment-heading::before,
  .appointment-heading::after {
    content: ""; flex: 1; height: 2px; background: var(--paper);
  }
  .appointment-box {
    position: absolute; left: 63px; top: 90px; width: 479px; height: 200px;
    background: var(--paper); border-radius: 16px; overflow: hidden;
  }
  .appointment-box .watermark {
    position: absolute; left: 0; right: 0; top: 78px; text-align: center;
    color: var(--faint); font-weight: 700; font-size: 34px;
  }
  .appointment-box .write-line {
    position: absolute; left: 0; right: 0; height: 3px; background: var(--ink);
  }

  /* Contact side */
  .card--contact {
    left: 297px; top: 515px; width: 608px; height: 347px;
    background: var(--paper);
  }
  .card--contact .corners { position: absolute; inset: 0; }
  .brand {
    position: absolute; left: 58px; top: 150px;
    display: flex; align-items: center; gap: 10px;
    color: var(--ink); font-weight: 700; font-size: 24px;
  }
  .brand .mark { width: 22px; height: 22px; border-radius: 50%; background: var(--ink); }
  .identity { position: absolute; left: 293px; top: 78px; color: var(--ink); }
  .identity .name { font-weight: 700; font-size: 24px; line-height: 34px; }
  .identity .title { font-size: 19px; line-height: 28px; }
  .contact-list { position: absolute; left: 292px; top: 162px; list-style: none; color: var(--ink); }
  .contact-list li {
    display: flex; align-items: flex-start; gap: 14px;
    font-style: italic; font-size: 17px; line-height: 21px; margin-bottom: 9px;
  }
  .contact-list li.address { margin-top: 14px; }
  .contact-list svg { width: 24px; height: 21px; flex: none; }
</style>
</head>
<body>
<div class="canvas">

  <section class="card card--appointment" aria-label="Appointment card">
    <h2 class="appointment-heading">NEXT APPOINTMENT</h2>
    <div class="appointment-box">
      <span class="watermark" aria-hidden="true">Vintner Dental</span>
      <span class="write-line" style="top:48px"></span>
      <span class="write-line" style="top:98px"></span>
      <span class="write-line" style="top:148px"></span>
    </div>
  </section>

  <section class="card card--contact" aria-label="Contact card">
    <svg class="corners" width="608" height="347" viewBox="0 0 608 347" aria-hidden="true">
      <polygon points="0,0 175,0 0,121" fill="#000"/>
      <polygon points="608,227 608,347 435,347" fill="#000"/>
    </svg>

    <div class="brand"><span class="mark"></span>Vintner Dental</div>

    <div class="identity">
      <h1 class="name">Dr MARLO VINTNER</h1>
      <p class="title">Doctor of Dental Medicine</p>
    </div>

    <ul class="contact-list">
      <li>
        <svg viewBox="0 0 24 21" aria-hidden="true"><path d="M2 7c0-3 4-5 10-5s10 2 10 5v2h-5V7H7v2H2z M5 11h14l2 8H3z" fill="#000"/><circle cx="12" cy="15" r="2.5" fill="#fff"/></svg>
        <span>514-629-5074</span>
      </li>
      <li>
        <svg viewBox="0 0 24 21" aria-hidden="true"><rect x="1" y="3" width="22" height="15" rx="1" fill="#000"/><path d="M2 4l10 8 10-8" stroke="#fff" stroke-width="1.6" fill="none"/></svg>
        <span>email@domain.com</span>
      </li>
      <li class="address">
        <svg viewBox="0 0 24 21" aria-hidden="true"><path d="M12 0a8 8 0 0 1 8 8c0 5-8 13-8 13S4 13 4 8a8 8 0 0 1 8-8z" fill="#000"/><circle cx="12" cy="8" r="3" fill="#fff"/></svg>
        <span>5182 Ch. Birchfield<br>Montreal QC H2T 4B9</span>
      </li>
    </ul>
  </section>

</div>
</body>
</html>
```